Marketing Postcards

I recently changed real estate companies and want to redo some advertising postcards I've used in the past. I want to replicate the existing cards with updated company info. Please see attached for proofs of old cards as well as the new company logo.

Industry/Entity Type

Real Estate

```html
<!DOCTYPE html>
<html lang="en">
<head>
<meta charset="utf-8">
<title>Marketing Postcard – Marlene Hadley</title>
<link rel="stylesheet" href="https://fonts.googleapis.com/css2?family=Oswald:wght@300;400&family=Pathway+Gothic+One&family=Sue+Ellen+Francisco&display=swap">
<style>
  :root {
    --paper: #ffffff;
    --ink: #111111;
    --script-ink: #555555;
    --body-grey: #5a5a5a;
    --brand-grey: #7b7b7b;
    --brand-text: #ffffff;
    --rule: #222222;
    --photo-light: #bdbdbd;
    --photo-dark: #6e6e6e;
  }
  * { margin: 0; padding: 0; box-sizing: border-box; }
  html, body { width: 1200px; height: 808px; overflow: hidden; background: var(--paper); }
  .postcard { position: relative; width: 1200px; height: 808px; background: var(--paper); color: var(--ink); }

  .agent-photo {
    position: absolute; left: 39px; top: 70px; width: 184px; height: 276px;
    border-radius: 12px;
    background: linear-gradient(160deg, var(--photo-light), var(--photo-dark));
  }

  .agent-details > * { position: absolute; left: 248px; line-height: 1; white-space: nowrap; }
  .script { font-family: "Sue Ellen Francisco", cursive; color: var(--script-ink); }
  .call-today { top: 28px; font-size: 70px; letter-spacing: 4px; }
  .agent-name { top: 112px; font-family: "Oswald", sans-serif; font-weight: 400; font-size: 44px; letter-spacing: -0.5px; }
  .agent-phone { top: 171px; font-family: "Oswald", sans-serif; font-weight: 400; font-size: 42px; }
  .agent-email { top: 223px; font-family: "Oswald", sans-serif; font-weight: 300; font-size: 32px; }
  .agent-site { top: 257px; font-family: "Oswald", sans-serif; font-weight: 300; font-size: 32px; }
  .agent-brokerage { top: 298px; font-family: "Pathway Gothic One", sans-serif; font-size: 24px; }
  .tagline { top: 332px; font-size: 42px; letter-spacing: 1px; }

  .divider { position: absolute; left: 699px; top: 38px; width: 2px; height: 270px; background: var(--rule); }

  .company { position: absolute; left: 720px; top: 36px; width: 470px; }
  .company-mark {
    width: 435px; height: 94px; background: var(--brand-grey);
    display: flex; align-items: center; justify-content: center; gap: 14px;
  }
  .company-mark .dot { width: 22px; height: 22px; border-radius: 50%; background: var(--brand-text); }
  .company-name { font-family: "Oswald", sans-serif; font-weight: 400; font-size: 34px; color: var(--brand-text); letter-spacing: 2px; text-transform: uppercase; }
  .company-address { font-family: "Oswald", sans-serif; font-weight: 400; font-size: 24px; margin-top: 12px; line-height: 1.2; white-space: nowrap; }
  .pledge-title { font-family: "Oswald", sans-serif; font-weight: 400; font-size: 19px; margin-top: 4px; line-height: 1.3; white-space: nowrap; }
  .pledge-text { font-family: "Pathway Gothic One", sans-serif; font-size: 20px; line-height: 24.5px; color: var(--body-grey); margin-top: 4px; white-space: nowrap; }
</style>
</head>
<body>
<main class="postcard">
  <div class="agent-photo" role="img" aria-label="Portrait photo of the agent"></div>

  <section class="agent-details">
    <p class="script call-today">Call Today!</p>
    <h1 class="agent-name">Marlene Hadley</h1>
    <p class="agent-phone">555-214-3870</p>
    <p class="agent-email">HomesByMarlene@mailbox.com</p>
    <p class="agent-site">www.CoastalPlainHomeFinder.com</p>
    <p class="agent-brokerage">Harborline Home Partners, Hometown Agents</p>
    <p class="script tagline">With you every step of the way!</p>
  </section>

  <div class="divider"></div>

  <section class="company">
    <div class="company-mark">
      <span class="dot"></span>
      <span class="company-name">Keystone Realty</span>
    </div>
    <p class="company-address">2180 Larkspur Avenue Riverton, NC 28590</p>
    <h2 class="pledge-title">Complete Confidentiality &amp; No Obligation Pledge</h2>
    <p class="pledge-text">Meetings, assessments and correspondence are kept solely between the<br>homeowner and/or the designated representative and do not require<br>a commitment. It is our passion to respond promptly to real estate<br>questions and see creative solutions no matter how great the vision.</p>
  </section>
</main>
</body>
</html>
```